Norwegian Mobile Home/Cabin Producer Needs Brochure Design

We make and deliver our own brand of mobile homes especially made for Norway and it's weather conditions. We differ from other brands in building quality in regards to a much more solid construction, insulation and choices. We work with our customer from the beginning and build them after their demands and wishes.
We need a brochure that holds us out as top of the line. We deliver mobile homes of all kinds and sizes. Both to the private and professional sector.
For the professional sector, mainly camping sites we want to show, lodges-, sanitary- and kitchen wagoons etc.
So we need a brochure of 14-20 pages in A4 where the double pages can be printed in A3 format.
We have logo (provided). But we need cover as well as back suggestions.
It should start with pages where we can teel who we are and stand for.Piicture(s) and space for some editable text (which we can write in norwegian). The text part can have a transparent background......or not. Give us your best shot. Also a smaller part in the private sector that shows winter time.
We want other pages for the private sector that shows what we deliver and the possibilities of choices.
Pages for the the professional sector.
Pages that show our production. How we transport. And the split construction. Only pictures from this portfolio here. (see fotoskap portfolios)
Take a look at provided pictures and our website www.solvikhytta.no for inspiration.
Here's a FotoSkap link to Pictures to choose from. http://bildelagr.example/K4TQ9P
(Hope it Works, let me know if not)
Our company name in small letters "fjordgrønn hyttebygg" means directly translated "fjordgreen cabin builds".
Looking forward to your suggestions.
Target Market(s)
Private market for vacation mobile homes. Camping sites and similar
Industry/Entity Type
Insulation
Requirements
Must have
- Our logo on the front page. Simple but inviting and professional
Logo and address on the back.

```html
<!DOCTYPE html>
<html lang="en">
<head>
<meta charset="utf-8">
<title>Brochure spread – About us</title>
<link rel="stylesheet" href="https://fonts.googleapis.com/css2?family=Arimo:wght@400;700&family=Inter:wght@200;300&display=swap">
<style>
  :root {
    --backdrop: #ececec;
    --paper: #ffffff;
    --ink: #1a1a1a;
    --heading-ink: #2a2a2a;
    --tint: rgba(70, 215, 240, 0.72);
    --photo-warm-1: #d9d2c6;
    --photo-warm-2: #b7a894;
    --photo-warm-3: #8a7a66;
    --photo-light: #f3f1ec;
    --heart-blue: rgba(110, 215, 240, 0.55);
  }
  html, body {
    margin: 0;
    padding: 0;
    width: 1200px;
    height: 900px;
    overflow: hidden;
    background: var(--backdrop);
  }
  .spread {
    position: absolute;
    left: 28px;
    top: 48px;
    width: 1142px;
    height: 800px;
    background: var(--paper);
    font-family: "Arimo", Arial, sans-serif;
    color: var(--ink);
  }
  .interior-photo {
    position: absolute;
    left: 0;
    top: 0;
    width: 745px;
    height: 514px;
    background:
      radial-gradient(ellipse at 28% 40%, var(--photo-light) 0%, transparent 45%),
      radial-gradient(ellipse at 55% 85%, var(--photo-warm-2) 0%, transparent 50%),
      linear-gradient(180deg, var(--photo-light) 0%, var(--photo-warm-1) 35%, var(--photo-warm-2) 75%, var(--photo-warm-3) 100%);
  }
  .tint-panel {
    position: absolute;
    left: 572px;
    top: 0;
    width: 173px;
    height: 514px;
    background: var(--tint);
  }
  .section-heading {
    position: absolute;
    margin: 0;
    writing-mode: vertical-rl;
    transform: rotate(180deg);
    font-family: "Inter", Helvetica, sans-serif;
    font-weight: 200;
    font-size: 30px;
    line-height: 1;
    color: var(--heading-ink);
    white-space: nowrap;
  }
  .section-copy {
    position: absolute;
    width: 222px;
    margin: 0;
    font-size: 11.2px;
    line-height: 15.2px;
  }
  .section-copy strong {
    display: block;
    font-weight: 700;
    font-size: 11.6px;
  }
  .about .section-heading { left: 246px; top: 582px; }
  .about .section-copy { left: 300px; top: 580px; }
  .who .section-heading { left: 817px; top: 80px; }
  .who .section-copy { left: 872px; top: 78px; }
  .what .section-heading { left: 817px; top: 324px; }
  .what .section-copy { left: 872px; top: 322px; }
  .heart-art {
    position: absolute;
    left: 792px;
    top: 492px;
    width: 320px;
    height: 308px;
    background: radial-gradient(ellipse at 50% 45%, var(--heart-blue) 0%, rgba(110, 215, 240, 0.25) 45%, transparent 70%);
  }
</style>
</head>
<body>
  <main class="spread">
    <div class="interior-photo" role="img" aria-label="Bright cabin living room with sofa, white tables, lilies, wooden floor and curtained windows"></div>
    <div class="tint-panel"></div>

    <section class="about">
      <h2 class="section-heading">About us</h2>
      <p class="section-copy"><strong>Voluptaspero volestia velit milicient.</strong>Moluptas veni omnis dolore mi, illecus vene ipsus volorem olupta sam repro qui ipsa nos que rem restionem eatis consequ aestibus, eatemolum doluptatio qui dentiam estemol orrumquamus nihit volore ratur sumquas piendi quam sus modiae autem expelique odit que ad ma aut eatusan delignam nobis et occabore nimpero te officilla voluptaes conecernatem eatur ad ut ex estio modis</p>
    </section>

    <section class="who">
      <h2 class="section-heading">Who we are</h2>
      <p class="section-copy"><strong>Agniti as cum quae sam, seceario</strong>mi, quaestrum quia et evelese quatet pliquias dende vendiatem quo dolorem ius adipsuntis enecto excerum lignis dolene raecest verum, cusdam, od maionse quatiur, sapid que estiam aut vendaepe parum voloreium ipi.</p>
    </section>

    <section class="what">
      <h2 class="section-heading">What we do</h2>
      <p class="section-copy"><strong>Agniti as cum quae sam, seceario</strong>mi, quaestrum quia et evelese quatet pliquias dende vendiatem quo dolorem ius adipsuntis enecto excerum lignis dolene raecest verum, cusdam, od maionse quatiur, sapid que estiam aut vendaepe parum voloreium ipiti restibus endis re voluptaturis eatem fugitae.</p>
    </section>

    <div class="heart-art" role="img" aria-label="Hand-drawn light blue crayon heart"></div>
  </main>
</body>
</html>
```